RBK TRAVEL CHARTER COMPANY
Charter Service
Project: RBK TRAVEL CHARTER COMPANY
RBK TRAVEL CHARTER COMPANY -
Creative Brief
Professional
Dom & Priscilla Hartwell
Owners
3487 N. Belcourt Ave. Compton, CA 90221
dom0734@quintmail.example
rbktravelcharter.example
Services: school trips/events excursions/visits company functions family events/picnics wedding/dinner shuttle bus services regular transport/pick up funerals/religious functions all bus transportation needs

```html
<!DOCTYPE html>
<html lang="en">
<head>
<meta charset="utf-8">
<title>RBK Travel Charter Company – Stationery</title>
<link rel="stylesheet" href="https://fonts.googleapis.com/css2?family=Arimo:wght@400;700&display=swap">
<style>
  :root {
    --ink: #231f20;
    --charcoal: #2b2929;
    --red: #d7262c;
    --paper: #ffffff;
    --stage: #ffffff;
    --line: #d9d9d9;
    --fold: #555555;
  }
  * { box-sizing: border-box; margin: 0; padding: 0; }
  html, body { width: 1200px; height: 737px; overflow: hidden; background: var(--stage); }
  body { font-family: "Arimo", Arial, sans-serif; color: var(--ink); position: relative; }

  .sheet { position: absolute; background: var(--paper); overflow: hidden; }
  .sheet--outlined { box-shadow: 0 0 0 1px var(--line); }
  .swoosh { position: absolute; left: 0; bottom: 0; width: 100%; display: block; }
  address { font-style: normal; }

  .brand { position: absolute; display: flex; align-items: center; gap: 6px; }
  .brand__mark { width: 10px; height: 10px; background: var(--red); flex: none; }
  .brand__name { font-weight: 700; color: var(--ink); letter-spacing: .04em; text-transform: uppercase; line-height: 1.05; }
  .brand--light .brand__name { color: var(--paper); }

  /* Letterhead */
  .letterhead { left: 12px; top: 7px; width: 555px; height: 705px; }
  .letterhead .brand { left: 22px; top: 24px; }
  .letterhead .brand__name { font-size: 15px; width: 150px; }
  .letterhead__contact { position: absolute; right: 26px; bottom: 14px; color: var(--paper); font-size: 8.5px; line-height: 1.4; }

  /* Envelope front */
  .envelope-front { left: 583px; top: 7px; width: 595px; height: 276px; }
  .envelope-front .brand { left: 22px; top: 22px; }
  .envelope-front .brand__name { font-size: 14px; width: 140px; }
  .envelope-front__return { position: absolute; left: 22px; bottom: 30px; color: var(--paper); font-size: 10px; line-height: 1.5; }

  /* Envelope back */
  .envelope-back { left: 583px; top: 317px; width: 595px; height: 240px; background: var(--charcoal); }

  /* Business card front */
  .card-front { left: 583px; top: 585px; width: 245px; height: 125px; }
  .card-front .brand { left: 12px; top: 10px; }
  .card-front .brand__mark { width: 7px; height: 7px; }
  .card-front .brand__name { font-size: 9px; width: 150px; }
  .card-front__owner { position: absolute; left: 12px; bottom: 16px; color: var(--paper); font-size: 7px; line-height: 1.4; }
  .card-front__owner strong { font-size: 7.5px; }
  .card-front__contact { position: absolute; right: 10px; bottom: 10px; color: var(--paper); font-size: 5.5px; line-height: 1.45; }

  /* Business card back */
  .card-back { left: 845px; top: 585px; width: 333px; height: 125px; background: var(--charcoal); }
  .card-back .brand { left: 18px; top: 46px; }
  .card-back .brand__name { font-size: 11px; width: 110px; }
  .services { position: absolute; left: 192px; top: 8px; bottom: 8px; padding-left: 12px; border-left: 1px solid var(--red); list-style: none; color: var(--paper); font-size: 6px; line-height: 1.9; }
</style>
</head>
<body>

  <section class="sheet sheet--outlined letterhead" aria-label="Letterhead">
    <div class="brand"><span class="brand__mark"></span><span class="brand__name">RBK Travel Charter Company</span></div>
    <svg class="swoosh" viewBox="0 0 555 150" height="150" preserveAspectRatio="none" aria-hidden="true">
      <path d="M0 40 C160 92 360 100 555 20 L555 150 L0 150 Z" fill="var(--red)"/>
      <path d="M0 52 C160 104 360 112 555 32 L555 150 L0 150 Z" fill="var(--paper)"/>
      <path d="M0 58 C160 110 360 118 555 38 L555 150 L0 150 Z" fill="var(--charcoal)"/>
    </svg>
    <address class="letterhead__contact">
      3487 N. Belcourt Ave.<br>Compton, CA 90221<br>Phone: 310-555-0142<br>Fax: 310-555-0187<br>rbktravelcharter.example
    </address>
  </section>

  <section class="sheet sheet--outlined envelope-front" aria-label="Envelope front">
    <div class="brand"><span class="brand__mark"></span><span class="brand__name">RBK Travel Charter Company</span></div>
    <svg class="swoosh" viewBox="0 0 595 170" height="170" preserveAspectRatio="none" aria-hidden="true">
      <path d="M0 8 C120 40 250 90 595 28 L595 170 L0 170 Z" fill="var(--red)"/>
      <path d="M0 20 C120 52 250 102 595 40 L595 170 L0 170 Z" fill="var(--paper)"/>
      <path d="M0 26 C120 58 250 108 595 46 L595 170 L0 170 Z" fill="var(--charcoal)"/>
    </svg>
    <address class="envelope-front__return">3487 N. Belcourt Ave.<br>Compton, CA 90221</address>
  </section>

  <section class="sheet envelope-back" aria-label="Envelope back">
    <svg width="595" height="240" viewBox="0 0 595 240" aria-hidden="true">
      <path d="M0 0 L595 0 L595 22 C445 22 355 88 297 88 C240 88 150 22 0 22 Z" fill="var(--paper)"/>
      <path d="M0 22 C150 22 240 88 297 88 C355 88 445 22 595 22" fill="none" stroke="var(--fold)" stroke-width="1"/>
    </svg>
  </section>

  <section class="sheet sheet--outlined card-front" aria-label="Business card front">
    <div class="brand"><span class="brand__mark"></span><span class="brand__name">RBK Travel Charter Company</span></div>
    <svg class="swoosh" viewBox="0 0 245 95" height="95" preserveAspectRatio="none" aria-hidden="true">
      <path d="M0 8 C70 26 150 30 245 6 L245 95 L0 95 Z" fill="var(--red)"/>
      <path d="M0 13 C70 31 150 35 245 11 L245 95 L0 95 Z" fill="var(--paper)"/>
      <path d="M0 16 C70 34 150 38 245 14 L245 95 L0 95 Z" fill="var(--charcoal)"/>
    </svg>
    <p class="card-front__owner"><strong>Dom &amp; Priscilla Hartwell</strong><br>Owners</p>
    <address class="card-front__contact">
      3487 N. Belcourt Ave.<br>Compton, CA 90221<br>Ph: 310-555-0142<br>Fax: 310-555-0187<br>dom0734@quintmail.example<br>rbktravelcharter.example
    </address>
  </section>

  <section class="sheet card-back" aria-label="Business card back">
    <div class="brand brand--light"><span class="brand__mark"></span><span class="brand__name">RBK Travel Charter Company</span></div>
    <ul class="services">
      <li>School Trips/Events</li>
      <li>Excursions/Visits</li>
      <li>Company Functions</li>
      <li>Family Events/Picnics</li>
      <li>Wedding/Dinner</li>
      <li>Shuttle Bus Services</li>
      <li>Regular Transport/Pick Up</li>
      <li>Funerals/Religious Functions</li>
      <li>All Bus Transportation Needs</li>
    </ul>
  </section>

</body>
</html>
```